Menu for Harbor Lantern Taproom a community and college bar

we want to have a colorful menu with pictures of our food
1 sheet two sided possibly between 8 x10 and 11 x 17
We want it to project a sports youthful fun atmosphere
quality food and spirits. We have an inside bar and an outside bar in an enclosed courtyard. Games and entertainment will be provided. Multiple TV's for all sports.
GLF Weekend Pass will be featuring all the Sunday GLF games
Updates

Target Market(s)

college age to middle age
sports fans football baseball basketball

Industry/Entity Type

College

Font styles to use
Sans Serif

Requirements
Must have
• logo as attached
• address, phone number, email address and web address
• pictures of food
Nice to have
• food pictures with brief description of items
• number of items
• appetizers -8
• soup/salads 6
• courses- 12
• deserts 5
Should not have
• cartoon pictures

```html
<!DOCTYPE html>
<html lang="en">
<head>
<meta charset="utf-8">
<title>Harbor Lantern Taproom – Sports Bar and Grill Menu</title>
<link href="https://fonts.googleapis.com/css2?family=Cabin:ital,wght@0,400;0,600;1,400;1,500&family=Lobster&family=Roboto+Condensed:wght@700&display=swap" rel="stylesheet">
<style>
  :root {
    --teal: #25b39c;
    --teal-bright: #3fd8c2;
    --purple: #9b3f9c;
    --yellow: #f6c431;
    --ink: #1b1b1b;
    --paper: #ffffff;
    --stage: #ececec;
    --copy-dark: #2a2a2a;
  }
  html, body {
    margin: 0;
    width: 1200px;
    height: 1200px;
    overflow: hidden;
    background: var(--stage);
  }
  .menu {
    position: absolute;
    left: 120px;
    top: 0;
    width: 650px;
    height: 812px;
    transform: scale(1.4778);
    transform-origin: 0 0;
    background: var(--paper);
    overflow: hidden;
    font-family: "Cabin", sans-serif;
  }
  .menu-art { position: absolute; inset: 0; }

  .brand-seal {
    position: absolute;
    left: 55px; top: 12px;
    width: 184px; height: 184px;
    border-radius: 50%;
    background: var(--paper);
    border: 5px solid var(--purple);
    box-sizing: border-box;
    display: flex; align-items: center; justify-content: center;
    text-align: center;
  }
  .brand-name {
    font-family: "Cabin", sans-serif;
    font-weight: 600;
    font-size: 19px;
    line-height: 1.15;
    color: var(--ink);
    text-transform: uppercase;
    letter-spacing: 1px;
  }

  .menu-title {
    position: absolute;
    right: 28px; top: 32px;
    margin: 0;
    font-family: "Lobster", cursive;
    font-weight: 400;
    font-size: 44px;
    line-height: 1;
  }
  .menu-title .lead { color: var(--teal); }
  .menu-title .tail { color: var(--purple); }

  .section-head {
    font-family: "Roboto Condensed", sans-serif;
    font-weight: 700;
    font-size: 10.5px;
    letter-spacing: 0.3px;
    text-transform: uppercase;
    margin: 0;
    padding-bottom: 4px;
    border-bottom: 1px solid;
  }
  .section-head .accent { color: var(--teal); }

  .starters {
    position: absolute;
    left: 24px; top: 226px;
    width: 258px;
  }
  .starters .section-head {
    color: #fff;
    width: 188px;
    padding-left: 10px;
    border-color: #9a9a9a;
    margin-bottom: 10px;
  }
  .dish { margin: 0 0 8px 8px; }
  .dish-name {
    font-style: italic;
    font-weight: 500;
    font-size: 11.5px;
    line-height: 16px;
    margin: 0;
  }
  .dish-desc {
    font-size: 8px;
    line-height: 14px;
    margin: 0;
  }
  .starters .dish-name { color: var(--teal-bright); }
  .starters .dish-desc { color: #f2f2f2; }

  .salads {
    position: absolute;
    left: 306px; top: 146px;
    width: 218px;
  }
  .salads .section-head {
    color: var(--teal);
    width: 188px;
    padding-left: 8px;
    border-color: var(--purple);
    margin-bottom: 6px;
  }
  .salads-note {
    margin: 0 0 12px 8px;
    font-style: italic;
    font-size: 10.5px;
    line-height: 14px;
    color: var(--teal);
  }
  .salads .dish-name { color: var(--purple); }
  .salads .dish-desc { color: var(--copy-dark); }
</style>
</head>
<body>
<main class="menu">
  <svg class="menu-art" width="650" height="812" viewBox="0 0 650 812" aria-hidden="false">
    <defs>
      <linearGradient id="column-shade" x1="0" y1="0" x2="1" y2="0">
        <stop offset="0" stop-color="#151515"/>
        <stop offset="0.6" stop-color="#3a3a3a"/>
        <stop offset="1" stop-color="#202020"/>
      </linearGradient>
      <linearGradient id="juice-tones" x1="0" y1="0" x2="1" y2="0">
        <stop offset="0" stop-color="#7a1b3a"/>
        <stop offset="0.3" stop-color="#d11d49"/>
        <stop offset="0.55" stop-color="#f08a22"/>
        <stop offset="0.8" stop-color="#5cb83a"/>
        <stop offset="1" stop-color="#c9392a"/>
      </linearGradient>
      <linearGradient id="beer-tones" x1="0" y1="0" x2="0" y2="1">
        <stop offset="0" stop-color="#5a2a12"/>
        <stop offset="0.4" stop-color="#f3efe6"/>
        <stop offset="1" stop-color="#e9a524"/>
      </linearGradient>
      <linearGradient id="food-tones" x1="0" y1="0" x2="1" y2="0">
        <stop offset="0" stop-color="#6a1c2a"/>
        <stop offset="0.5" stop-color="#a3283a"/>
        <stop offset="1" stop-color="#4d1a1f"/>
      </linearGradient>
    </defs>

    <!-- dark left column -->
    <path d="M0,130 Q330,92 650,128 L650,140 Q330,108 287,118 L287,812 L0,812 Z" fill="url(#column-shade)"/>
    <rect x="0" y="130" width="287" height="682" fill="url(#column-shade)"/>
    <!-- purple header stripe -->
    <path d="M0,124 Q330,86 650,122 L650,136 Q330,100 0,136 Z" fill="var(--purple)"/>

    <!-- dark lower right field with yellow swoosh -->
    <path d="M287,700 Q400,430 650,395 L650,410 Q420,450 300,700 Z" fill="var(--yellow)"/>
    <path d="M300,700 Q420,450 650,410 L650,720 L287,720 Z" fill="var(--ink)"/>

    <g role="img" aria-label="Beer bottle pouring into a frothy mug of lager">
      <rect x="560" y="135" width="90" height="290" rx="30" fill="url(#beer-tones)"/>
    </g>
    <g role="img" aria-label="Strawberry ice cream sundae in a glass">
      <rect x="287" y="410" width="88" height="150" rx="30" fill="#f2c6d2"/>
    </g>
    <g role="img" aria-label="Glasses of beet, orange and green juice with fresh vegetables">
      <rect x="290" y="490" width="360" height="205" rx="10" fill="url(#juice-tones)"/>
    </g>

    <!-- bottom food band -->
    <path d="M0,812 L0,780 Q300,710 650,700 L650,812 Z" fill="var(--purple)"/>
    <g role="img" aria-label="Plate of glazed chicken wings">
      <path d="M70,812 L70,752 Q330,712 650,708 L650,812 Z" fill="url(#food-tones)"/>
    </g>
    <path d="M70,754 Q330,708 650,703" fill="none" stroke="var(--yellow)" stroke-width="5"/>
    <g role="img" aria-label="Grilled meat skewers on a board">
      <rect x="505" y="712" width="145" height="100" rx="12" fill="#6b3a1e"/>
    </g>
    <g role="img" aria-label="Smiling chef in a white hat making an OK sign">
      <rect x="10" y="676" width="96" height="136" rx="20" fill="#e4e4e4"/>
    </g>
  </svg>

  <div class="brand-seal">
    <span class="brand-name">Harbor Lantern<br>Taproom</span>
  </div>

  <h1 class="menu-title"><span class="lead">Sports Bar</span> <span class="tail">and Grill</span></h1>

  <section class="starters">
    <h2 class="section-head"><span class="accent">Starting</span> Line Up</h2>
    <div class="dish">
      <p class="dish-name">Corn nuggets</p>
      <p class="dish-desc">Creamy corn mixture battered and fried golden brown</p>
    </div>
    <div class="dish">
      <p class="dish-name">Fried Mac n Cheese bites</p>
      <p class="dish-desc">Creamy mac n cheese battered and fried and served<br>with your choice of dipping sauce</p>
    </div>
    <div class="dish">
      <p class="dish-name">Chili cheese fries</p>
      <p class="dish-desc">Your choice of fries or tots topped with Harbor Lantern Chili,<br>queso, shredded cheese blend, diced tomatoes, and jalapenos</p>
    </div>
    <div class="dish">
      <p class="dish-name">Loaded Potato Slabs</p>
      <p class="dish-desc">Potato slices topped with BBQ pork, cheddar cheese,<br>and green onions served with a side of ranch</p>
    </div>
    <div class="dish">
      <p class="dish-name">Southwest Spring Rolls</p>
      <p class="dish-desc">Chicken, black beans, corn, peppers, jalapeños and<br>jack cheese wrapped inside a tortilla and fried golden<br>brown served with a homemade chipotle ranch sauce</p>
    </div>
    <div class="dish">
      <p class="dish-name">Fried Oysters</p>
      <p class="dish-desc">One dozen oysters fried golden brown and served with cocktail</p>
    </div>
    <div class="dish">
      <p class="dish-name">Chips and Queso</p>
      <p class="dish-desc">Creamy 4 cheese blend topped with diced tomatoes<br>and jalapeños and side of salsa</p>
    </div>
    <div class="dish">
      <p class="dish-name">Tavern Nachos</p>
      <p class="dish-desc">Your choice of chicken or beef on a bed of tortilla<br>chips topped with queso, shredded cheese,<br>shredded lettuce, Pico, and jalapenos</p>
    </div>
  </section>

  <section class="salads">
    <h2 class="section-head">Salads and Wraps</h2>
    <p class="salads-note">*Can be ordered as a salad or wrap*<br>Add chicken| Add Steak</p>
    <div class="dish">
      <p class="dish-name">House</p>
      <p class="dish-desc">Romaine lettuce topped with cucumbers, tomatoes,<br>onions, cheese and your choice of dressing</p>
    </div>
    <div class="dish">
      <p class="dish-name">Classic Caesar</p>
      <p class="dish-desc">A bed of romaine lettuce topped with creamy<br>Caesar dressing, parmesan cheese, and croutons</p>
    </div>
    <div class="dish">
      <p class="dish-name">Buffalo Chicken</p>
      <p class="dish-desc">A bed of romaine lettuce topped with buffalo chicken,<br>bleu cheese crumbles, and your choice of ranch<br>or bleu cheese dressing</p>
    </div>
  </section>
</main>
</body>
</html>
```